Research campaign for the global health issues in Africa must be modern, impactful and unique *

Please see attachment
Research campaign for the global health issues in Africa must be modern, impactful and unique
Updates

Please find the updated flyer requirement. These designs are not modern. We would need this flyer displayed on PV , Chatterloop and blurtwave. Please use either option of the requirement. Color scheme is Blue.

Target Market(s)

Patients, volunteers, patient advocacy groups, hospitals, healthcare professionals

Industry/Entity Type

Health Care

Font styles to use
Serif

Colors
0355a3
fbed22
f04a50

Requirements
Must have
• Please note that this must be a modern flyer that can be posted on Pictavine so size matters here.
Nice to have
• To see African/black people or foot print or shadow of a walk
• There can be a background image of a child’s face or Person walking or We could have a hand print or foot print with different disease colors.

```html
<!DOCTYPE html>
<html lang="en">
<head>
<meta charset="utf-8">
<title>Walk for Global Health Research Campaign 2019</title>
<link href="https://fonts.googleapis.com/css2?family=Roboto+Condensed:wght@300;400;700&display=swap" rel="stylesheet">
<style>
  :root {
    --navy: #1e2a5a;
    --teal: #138a8f;
    --teal-light: #4aa9b5;
    --brand-blue: #1f4e8a;
    --deep: #0e1a38;
    --mid-blue: #1b5d9c;
    --sky: #8fd0dc;
    --footer-cyan: #44a9c9;
    --white: #ffffff;
    --grey-text: #3a3f48;
  }
  * { margin: 0; padding: 0; box-sizing: border-box; }
  html, body { width: 927px; height: 1200px; overflow: hidden; background: #fff; }
  body { font-family: "Roboto Condensed", "Arial Narrow", sans-serif; }
  .flyer {
    position: relative; width: 927px; height: 1200px; overflow: hidden;
    background: linear-gradient(180deg, #f3f5f7 0%, #e7f0f4 35%, #bfe3ea 62%, var(--sky) 78%, #6cc0d0 84%);
  }
  .globe-art {
    position: absolute; left: 70px; top: 40px; width: 810px; height: 810px; border-radius: 50%;
    background: radial-gradient(circle at 50% 50%, rgba(205,232,240,0.7) 0%, rgba(170,215,228,0.45) 45%, rgba(150,210,225,0.2) 70%, rgba(255,255,255,0) 72%);
    border: 1px solid rgba(120,200,215,0.4);
  }
  .centered { position: absolute; left: 9px; width: 927px; text-align: center; line-height: 1; white-space: nowrap; }
  .walk-for { top: 115px; font-size: 21px; font-weight: 700; letter-spacing: 16px; color: var(--navy); }
  .title { top: 159px; font-size: 42px; font-weight: 700; color: var(--navy); }
  .commemoration { top: 226px; font-size: 35px; color: var(--teal); text-shadow: 0 1px 2px #fff; }
  .day { top: 272px; font-size: 45px; color: var(--teal); text-shadow: 0 1px 2px #fff; }
  .date { top: 377px; font-size: 35px; color: var(--navy); }
  .route { top: 423px; font-size: 26px; color: var(--grey-text); font-weight: 300; }
  .time { top: 471px; font-size: 43px; color: var(--navy); }
  .partners-label { top: 538px; font-size: 21px; color: var(--teal-light); font-weight: 300; }
  .partner-badge {
    position: absolute; top: 586px; width: 134px; height: 68px; border-radius: 12px;
    background: rgba(160,185,205,0.45);
  }
  .brand-name {
    position: absolute; left: 134px; top: 683px; display: flex; align-items: center; gap: 8px;
    font-size: 23px; line-height: 25px; font-weight: 700; color: var(--brand-blue); letter-spacing: 1px;
  }
  .brand-name .mark { width: 14px; height: 14px; background: var(--brand-blue); flex: none; }
  .commitment {
    position: absolute; left: 306px; top: 681px; font-size: 20.5px; line-height: 26px; color: var(--brand-blue); white-space: nowrap;
  }
  .waves { position: absolute; left: 0; top: 740px; width: 927px; height: 460px; }
  .badge { position: absolute; left: 700px; top: 770px; width: 204px; height: 204px; }
  .badge-text { position: absolute; left: 700px; top: 800px; width: 204px; text-align: center; color: var(--white); font-weight: 700; }
  .badge-text .free { font-size: 43px; line-height: 48px; }
  .badge-text .sub { font-size: 17.5px; line-height: 22px; }
  .benefits { position: absolute; left: 67px; top: 939px; width: 820px; color: var(--white); }
  .benefits h2 { font-size: 19.5px; line-height: 23px; font-weight: 700; margin-bottom: 17px; white-space: nowrap; }
  .benefits ul { list-style: none; }
  .benefits li { font-size: 16.5px; line-height: 20px; font-weight: 400; padding-left: 14px; position: relative; white-space: nowrap; }
  .benefits li::before { content: "•"; position: absolute; left: 0; }
  .divider { position: absolute; left: 30px; top: 1085px; width: 867px; height: 1px; background: rgba(90,160,210,0.5); }
  .contact { position: absolute; top: 1102px; font-size: 17.5px; line-height: 20px; color: var(--footer-cyan); font-weight: 300; font-style: normal; white-space: nowrap; }
</style>
</head>
<body>
<main class="flyer">
  <div class="globe-art" role="img" aria-label="Soft globe with a glowing network of connected lines"></div>

  <p class="centered walk-for">WALK FOR</p>
  <h1 class="centered title">GLOBAL HEALTH RESEARCH CAMPAIGN 2019</h1>
  <p class="centered commemoration">IN COMMEMORATION OF</p>
  <p class="centered day">THE WORLD CLINICAL TRIALS DAY</p>
  <p class="centered date">Saturday, May 25, 2019</p>
  <p class="centered route">Meridian Hospital Gate to Unity Stadium Eastside</p>
  <p class="centered time">7:00 am</p>
  <p class="centered partners-label">DISEASE FOCUS OF OUR PARTNERS</p>

  <div class="partner-badge" style="left:98px"></div>
  <div class="partner-badge" style="left:254px"></div>
  <div class="partner-badge" style="left:413px"></div>
  <div class="partner-badge" style="left:568px"></div>
  <div class="partner-badge" style="left:723px"></div>

  <div class="brand-name"><span class="mark"></span><span>VELTRIA<br>RESEARCH</span></div>
  <p class="commitment">VELTRIA RESEARCH IS COMMITTED TO FINDING INNOVATIVE<br>GLOBAL HEALTH SOLUTIONS THROUGH CLINICAL RESEARCH</p>

  <svg class="waves" viewBox="0 0 927 460" aria-hidden="true">
    <defs>
      <linearGradient id="deepBand" x1="0" y1="0" x2="0" y2="1">
        <stop offset="0" stop-color="#1b5d9c"/>
        <stop offset="0.45" stop-color="#163f74"/>
        <stop offset="1" stop-color="#0e1a38"/>
      </linearGradient>
    </defs>
    <path d="M0 70 C 200 150, 420 170, 927 60 L 927 460 L 0 460 Z" fill="url(#deepBand)"/>
    <path d="M0 62 C 180 140, 420 168, 730 125 C 620 150, 300 170, 0 88 Z" fill="#ffffff"/>
    <polyline points="0,40 540,40 572,-10 610,90 640,30 660,40 700,40 740,-50 780,95 820,25 845,40 880,0 927,40"
              fill="none" stroke="#ffffff" stroke-width="2" opacity="0.9"/>
  </svg>

  <svg class="badge" viewBox="0 0 204 204" aria-hidden="true">
    <polygon fill="#1c2b5a" stroke="#ffffff" stroke-width="3"
      points="102,4 113,18 129,8 135,25 153,20 154,38 172,38 167,55 184,60 174,75 189,86 175,97 186,111 170,118 177,134 160,137 162,155 145,154 142,172 126,166 118,182 104,172 92,184 83,169 67,177 62,160 45,163 45,145 28,143 33,126 17,119 27,105 14,94 28,84 20,68 37,63 34,46 51,45 53,27 70,31 76,14 91,21"/>
  </svg>
  <div class="badge-text">
    <div class="free">FREE</div>
    <div class="sub">HEALTH<br>SCREENING AND<br>CONSULTATION</div>
  </div>

  <section class="benefits">
    <h2>The potential benefits of participating in a clinical trial may include the following:</h2>
    <ul>
      <li>Access to promising new treatments often not available outside the clinical-trial setting</li>
      <li>Treatment that may be more effective than the standard approach</li>
      <li>The opportunity to be the first to benefit from a new method under study</li>
      <li>The chance to play an active role in your own health care and gain a greater understanding of your disease or condition</li>
    </ul>
  </section>

  <div class="divider"></div>
  <address class="contact" style="left:67px">Veltria Research Corporate Office<br>27 Harmon Street, Off Calder Avenue<br>Palmview, Lagos, Nigeria</address>
  <p class="contact" style="left:384px">Nigeria Office: +23 4800 555 0147<br>International: 1.555.010.2847 (USA)</p>
  <p class="contact" style="left:680px">info@veltriaresearch.com<br>www.veltriaresearch.com</p>
</main>
</body>
</html>
```